Project Sign for Construction Company

Site contractor needs a 4'x8' sign to place on construction sites for advertising. Our company builds the infrastructure for new housing developments. These sign will be posted on the road side to be viewed by passing cars. I want a clean and bold look and feel that resembles my company logo.

Font styles to use
Other font styles liked:
• Hypatia Sans Pro

Colors

Designer to choose colors to be used in the design.

Requirements
Must have
• 555-318-2946 | Info@MarlowTerraworks.example
• CUC 8841907
• www.MarlowTerraworks.example
• Services
• Road Construction
• Site Preparation & Excavation
• Underground Utilities
• Shoreline Restoration
Nice to have
• Now Hiring
• Pipe Layers
• Foremen
• Equipment Operators
Should not have
• Should not have stock picture images used in the design, focus on logo and geometric shapes

```html
<!DOCTYPE html>
<html lang="en">
<head>
<meta charset="utf-8">
<title>Marlow Terraworks – Site Sign</title>
<link href="https://fonts.googleapis.com/css2?family=Arimo:wght@400;700&display=swap" rel="stylesheet">
<style>
  :root {
    --brand-blue: #0b4188;
    --stripe-blue: #3f68a4;
    --steel-gray: #6b6b6b;
    --ink: #333333;
    --sign-white: #ffffff;
    --backdrop-light: #d2d2d2;
    --backdrop-dark: #a9a9a9;
  }
  * { margin: 0; padding: 0; box-sizing: border-box; }
  html, body { width: 1200px; height: 1200px; overflow: hidden; }
  body {
    background: radial-gradient(ellipse at center, var(--backdrop-light) 0%, var(--backdrop-dark) 100%);
    font-family: "Arimo", Arial, sans-serif;
    position: relative;
  }
  .sign {
    position: absolute;
    left: 21px; top: 310px;
    width: 1158px; height: 578px;
    background: var(--sign-white);
    overflow: hidden;
  }
  .top-band { position: absolute; left: 0; top: 0; }
  .brand-mark {
    position: absolute; left: 118px; top: 58px;
    width: 130px; height: 130px;
    background: var(--brand-blue);
  }
  .brand-name {
    position: absolute; left: 308px; top: 56px;
    color: var(--brand-blue);
    font-weight: 700;
    line-height: 1;
  }
  .brand-name .line-one { display: block; font-size: 100px; letter-spacing: 8px; }
  .brand-name .line-two { display: block; font-size: 44px; letter-spacing: 7px; margin-top: 8px; }
  .contact { position: absolute; left: 95px; top: 236px; color: var(--ink); }
  .phone {
    font-size: 84px; font-weight: 700; color: var(--brand-blue);
    line-height: 1; letter-spacing: -1px;
  }
  .website { font-size: 35px; margin-top: 12px; line-height: 1.1; }
  .email { font-size: 30px; margin-top: 10px; line-height: 1.1; }
  .license { font-size: 24px; margin-top: 8px; margin-left: -5px; }
  .services { position: absolute; left: 678px; top: 246px; }
  .services-title {
    width: 284px; height: 54px;
    background: var(--brand-blue); color: var(--sign-white);
    font-size: 40px; font-weight: 700;
    display: flex; align-items: center; justify-content: center;
  }
  .services-list { list-style: none; margin-top: 14px; margin-left: 18px; }
  .services-list li {
    font-size: 26px; color: var(--ink); line-height: 30px;
    position: relative; padding-left: 18px;
  }
  .services-list li::before {
    content: ""; position: absolute; left: 0; top: 10px;
    width: 10px; height: 10px; border-radius: 50%;
    background: var(--brand-blue);
  }
  .hiring { position: absolute; left: 92px; top: 473px; display: flex; align-items: center; }
  .hiring-tag { position: relative; width: 370px; height: 54px; }
  .hiring-tag svg { position: absolute; left: 0; top: 0; }
  .hiring-label {
    position: absolute; left: 34px; top: 0; height: 54px;
    display: flex; align-items: center;
    color: var(--sign-white); font-size: 42px; font-weight: 700;
  }
  .hiring-roles { font-size: 26px; color: var(--ink); margin-left: 4px; }
  .bottom-band {
    position: absolute; left: 0; bottom: 0; width: 100%; height: 34px;
    background: var(--stripe-blue);
  }
</style>
</head>
<body>
  <div class="sign">
    <svg class="top-band" width="1158" height="40" viewBox="0 0 1158 40">
      <polygon points="0,0 75,0 98,40 0,40" fill="#6b6b6b"/>
      <polygon points="265,0 1158,0 1158,40 287,40" fill="#0b4188"/>
    </svg>

    <div class="brand-mark" aria-hidden="true"></div>
    <div class="brand-name">
      <span class="line-one">MARLOW</span>
      <span class="line-two">TERRAWORKS</span>
    </div>

    <div class="contact">
      <div class="phone">555-318-2946</div>
      <div class="website">www.MarlowTerraworks.example</div>
      <div class="email">Info@MarlowTerraworks.example</div>
      <div class="license">CUC 8841907</div>
    </div>

    <div class="services">
      <div class="services-title">SERVICES</div>
      <ul class="services-list">
        <li>Road Construction</li>
        <li>Site Preparation &amp; Excavation</li>
        <li>Underground Utilities</li>
        <li>Shoreline Restoration</li>
      </ul>
    </div>

    <div class="hiring">
      <div class="hiring-tag">
        <svg width="370" height="54" viewBox="0 0 370 54">
          <polygon points="0,0 331,0 341,27 331,54 0,54" fill="#6b6b6b"/>
          <polygon points="338,0 349,0 360,27 349,54 338,54 349,27" fill="#0b4188"/>
        </svg>
        <span class="hiring-label">NOW HIRING</span>
      </div>
      <div class="hiring-roles">Pipe Layers | Foremen | Equipment Operators</div>
    </div>

    <div class="bottom-band" role="img" aria-label="Blue and white diagonal hazard stripe band along the bottom edge"></div>
  </div>
</body>
</html>
```